Home page design for Drone video business (the Business focusses on home videos for realtors)

Dear reader,

*I NEED DESIGNS OF ALL THE PAGES*
We need a first design of a homepage and of 4 other pages of the website of a business that sells drone video services. All the pages will need to be in the similar design style.
The video's are targeted at consumers that want to sell there home and would like to have a cool drone video of photos of their home.

How does the website look:
- has a navbar on top
- A cool looking banner of an areal drone.
- A Big header: with company name: SkyNestReels
- A smaller subheader: We film your home to increase your chances of sale
- Then a section with a Big header: How does it work
- In this section a place for a vimeo explainitory video
- Then a similar navbar styled bar with a phone number and a email address
- Then a section where the videos porfolio is displayed in a cool way
- Inside this sectiona header: Our work

- A section with header: Why us?
- 4 symbols here with a subheader and some lorum ipsum text underneath (see wireframe images)

- Under that a: Contact us
- where you can put in name, email, phone, message box and a send button

- At the bottom a footer with phone number and a fake address for now.

Be creative. Use creative but serious color.
Use a serious font. Make it a sharp design. Sharp lines. Not to dark design and not to light design.

The wireframes are the same kind of images.
PLEASE PUT IN DESIGNS OF ALL THE PAGES

Good luck

Target Market(s)

People that want to sell home and want to make a cool drone video or photos of their home.

Industry/Entity Type

Business

Contact Information for Business Card

Milo Brenning
milo@skynestreels.example
+31647283915

Logo Text

SkyNestReels

Number of Pages Required

1 page

Font styles to use
Sans Serif

Requirements
Must have
• All the sections as explained in the instructions.
• The nav bar should have an about us, services, portfolio and a contact us buttons.
• See instruction for details.
• Must include designs of the front page, contact us, our services, portfolio and contact us.
• If you do add some designs for the "about us", "services", "prices", "portfolio" and "contact us" pages, you make a way better chance of winning the competition.
Nice to have
• designs for the other pages as described at the Must haves. You make a better chance of winning if you include them. Look at the wireframes to see the mockups for those pages. think creative about what kind of sections and design should be included in those pages.
Should not have
• bad designs.

```html
<!DOCTYPE html>
<html lang="en">
<head>
<meta charset="utf-8">
<title>SkyNestReels – Home</title>
<link rel="stylesheet" href="https://fonts.googleapis.com/css2?family=Jost:wght@500;600;700&family=Open+Sans:wght@400;600&display=swap">
<style>
  :root{
    --gold:#d9a22b;
    --charcoal:#2b2a28;
    --black:#000;
    --white:#fff;
    --ink:#2b2a28;
    --muted:#d8d5cf;
    --field-line:#8a8a8a;
    --player:#111;
  }
  *{margin:0;padding:0;box-sizing:border-box}
  html,body{width:1200px;height:2571px;overflow:hidden}
  body{position:relative;background:var(--white);font-family:"Open Sans",sans-serif;color:var(--ink)}
  .abs{position:absolute}
  .display{font-family:"Jost",sans-serif;font-weight:700;text-transform:uppercase}

  /* hero */
  .hero{left:0;top:0;width:1200px;height:1008px;background:var(--black)}
  .hero-photo{left:0;top:0;width:1200px;height:566px;
    background:
      radial-gradient(circle at 965px 425px,#fff6cf 0,#ffd766 45px,rgba(240,150,40,.65) 120px,rgba(200,110,40,0) 330px),
      linear-gradient(180deg,#2f3036 0%,#5b4d45 30%,#a26a3c 62%,#c97b2c 82%,#3a2210 94%,#000 100%)}
  .brand{left:77px;top:30px;color:var(--white);font-family:"Jost",sans-serif;font-weight:700;font-size:22px;display:flex;align-items:center;gap:10px}
  .brand-dot{width:14px;height:14px;background:var(--white)}
  .nav{top:56px;left:725px;display:flex;gap:0}
  .nav a{position:absolute;top:0;color:var(--white);text-decoration:none;font-family:"Jost",sans-serif;font-weight:600;font-size:17px;white-space:nowrap}
  .hero-title{left:460px;top:282px;font-size:42px;color:var(--white);letter-spacing:.5px}
  .hero-sub{left:463px;top:330px;font-size:21px;line-height:25px;color:var(--gold)}

  .section-title{left:0;width:1200px;text-align:center;font-size:36px}
  .how-title{top:612px;color:var(--white)}
  .video-frame{left:391px;top:679px;width:418px;height:260px;background:var(--white);border-radius:14px}

  .video{position:absolute;overflow:hidden;border:3px solid var(--player);border-radius:3px}
  .video .shot{position:absolute;inset:0}
  .video .play{position:absolute;left:50%;top:44%;transform:translate(-50%,-50%)}
  .video .controls{position:absolute;left:0;right:0;bottom:0;background:var(--player)}

  /* contact strip */
  .strip{left:0;top:1008px;width:1200px;height:84px;background:var(--gold)}
  .strip-item{top:1032px;display:flex;align-items:center;gap:14px;color:var(--white);font-family:"Jost",sans-serif;font-weight:700;font-size:27px}

  .work-title{top:1144px;color:var(--ink)}

  /* why us */
  .why{left:0;top:1440px;width:1200px;height:471px}
  .why-title{top:1521px;color:var(--white)}
  .feature-icon{width:70px;height:70px}
  .feature-name{font-size:25px;color:var(--gold);line-height:1}
  .feature-text{width:240px;font-size:11.7px;line-height:14.5px;color:var(--muted)}

  /* contact form */
  .contact-title{top:1944px;color:var(--ink)}
  .field{left:240px;width:350px;height:38px;border:1.5px solid var(--field-line);font-size:12px;color:#555;padding:9px 12px;background:var(--white)}
  .field-message{left:610px;top:2030px;width:357px;height:147px}
  .send{left:240px;top:2194px;width:727px;height:45px;background:var(--gold);color:var(--white);text-align:center;line-height:45px;font-size:20px;letter-spacing:1px}

  /* footer */
  .footer{left:0;top:2323px;width:1200px;height:248px;background:var(--charcoal)}
  .social{top:2386px;left:553px;display:flex;gap:7px}
  .social span{width:27px;height:27px;background:var(--gold);border-radius:4px;display:block}
  .footer-brand{left:0;width:1200px;top:2450px;text-align:center;color:var(--white);font-family:"Jost",sans-serif;font-weight:700;font-size:15px}
  .footer-phone{left:0;width:1200px;top:2484px;text-align:center;color:var(--white);font-family:"Jost",sans-serif;font-weight:700;font-size:17px}
  .copyright{left:0;width:1200px;top:2512px;text-align:center;color:#aaa;font-size:10px}
</style>
</head>
<body>

<!-- Hero -->
<div class="abs hero"></div>
<div class="abs hero-photo" role="img" aria-label="Silhouette of a camera drone flying against an orange sunset sky over a dark tree line"></div>
<div class="abs brand"><span class="brand-dot"></span>SkyNestReels</div>
<nav class="abs nav">
  <a href="#services" style="left:0">Services</a>
  <a href="#about" style="left:101px">About Us</a>
  <a href="#portfolio" style="left:211px">Portfolio</a>
  <a href="#contact" style="left:315px">Contact Us</a>
</nav>
<h1 class="abs display hero-title">SkyNestReels</h1>
<p class="abs display hero-sub">We film your home to increase<br>chances of sale</p>

<!-- How it works -->
<h2 class="abs display section-title how-title">How does it work?</h2>
<div class="abs video-frame"></div>
<div class="video" style="left:412px;top:696px;width:374px;height:224px">
  <div class="shot" role="img" aria-label="Aerial view of a large house with a lawn surrounded by pine trees" style="background:linear-gradient(160deg,#3d6a3a,#6f8f4f 45%,#9a8f7a 60%,#4d6e39)"></div>
  <svg class="play" width="78" height="78" viewBox="0 0 78 78"><circle cx="39" cy="39" r="35" fill="rgba(0,0,0,.15)" stroke="#fff" stroke-width="4"/><path d="M30 22 L58 39 L30 56Z" fill="#fff"/></svg>
  <svg class="controls" width="368" height="18" viewBox="0 0 368 18"><rect width="368" height="18" fill="#111"/><g fill="#fff"><rect x="6" y="5" width="8" height="8"/><path d="M19 5l7 4-7 4z"/><rect x="28" y="5" width="2" height="8"/><rect x="32" y="5" width="2" height="8"/><path d="M40 7h3l4-3v10l-4-3h-3z"/><rect x="52" y="7" width="20" height="4" fill="#555"/><rect x="98" y="8.5" width="200" height="1.5" fill="#666"/><rect x="98" y="8.5" width="40" height="1.5"/><circle cx="138" cy="9" r="3"/><rect x="340" y="5" width="8" height="8" fill="none" stroke="#fff" stroke-width="1.5"/></g><text x="306" y="12" fill="#fff" font-size="6" font-family="Open Sans,sans-serif">0:25 / 9:33</text><text x="351" y="12" fill="#fff" font-size="8" font-family="Open Sans,sans-serif" font-weight="600">HD</text></svg>
</div>

<!-- Contact strip -->
<div class="abs strip"></div>
<div class="abs strip-item" style="left:183px">
  <svg width="22" height="26" viewBox="0 0 24 24"><path fill="#fff" d="M6.6 10.8c1.4 2.8 3.8 5.1 6.6 6.6l2.2-2.2c.3-.3.7-.4 1-.2 1.1.4 2.3.6 3.6.6.6 0 1 .4 1 1V20c0 .6-.4 1-1 1C10.6 21 3 13.4 3 4c0-.6.4-1 1-1h3.5c.6 0 1 .4 1 1 0 1.3.2 2.5.6 3.6.1.3 0 .7-.2 1z"/></svg>
  +31670418263
</div>
<div class="abs strip-item" style="left:738px">
  <svg width="36" height="24" viewBox="0 0 36 24"><rect width="36" height="24" fill="#fff"/><path d="M0 0 L18 13 L36 0" fill="none" stroke="#d9a22b" stroke-width="2.5"/></svg>
  contact@skynestreels.example
</div>

<!-- Our work -->
<h2 class="abs display section-title work-title">Our work</h2>
<div class="video" style="left:171px;top:1207px;width:271px;height:161px">
  <div class="shot" role="img" aria-label="Person launching a drone by hand at dusk over the sea" style="background:linear-gradient(180deg,#6f8fb4,#d6a08c 55%,#3a4e6a 80%,#222 100%)"></div>
  <svg class="play" width="62" height="62" viewBox="0 0 78 78"><circle cx="39" cy="39" r="35" fill="none" stroke="#fff" stroke-width="5"/><path d="M30 22 L58 39 L30 56Z" fill="#fff"/></svg>
  <svg class="controls" width="265" height="14" viewBox="0 0 265 14"><rect width="265" height="14" fill="#111"/><g fill="#fff"><rect x="5" y="4" width="6" height="6"/><path d="M14 4l5 3-5 3z"/><rect x="30" y="4" width="6" height="6"/><rect x="70" y="6.5" width="130" height="1" fill="#777"/><circle cx="95" cy="7" r="2"/></g><text x="248" y="10" fill="#fff" font-size="7" font-family="Open Sans,sans-serif">HD</text></svg>
</div>
<div class="video" style="left:465px;top:1207px;width:270px;height:161px">
  <div class="shot" role="img" aria-label="Aerial view of a hillside villa with a pool among green trees" style="background:linear-gradient(160deg,#4e7a3a,#8f8f6a 45%,#c3a27c 55%,#3f6a34)"></div>
  <svg class="play" width="62" height="62" viewBox="0 0 78 78"><circle cx="39" cy="39" r="35" fill="none" stroke="#fff" stroke-width="5"/><path d="M30 22 L58 39 L30 56Z" fill="#fff"/></svg>
  <svg class="controls" width="264" height="14" viewBox="0 0 264 14"><rect width="264" height="14" fill="#111"/><g fill="#fff"><rect x="5" y="4" width="6" height="6"/><path d="M14 4l5 3-5 3z"/><rect x="30" y="4" width="6" height="6"/><rect x="70" y="6.5" width="130" height="1" fill="#777"/><circle cx="95" cy="7" r="2"/></g><text x="247" y="10" fill="#fff" font-size="7" font-family="Open Sans,sans-serif">HD</text></svg>
</div>
<div class="video" style="left:758px;top:1207px;width:271px;height:161px">
  <div class="shot" role="img" aria-label="Aerial view of a white house with a grey roof beside tall trees" style="background:linear-gradient(150deg,#2f5f2c,#6f8a5a 40%,#c9cdd0 55%,#4c6e3a)"></div>
  <svg class="play" width="62" height="62" viewBox="0 0 78 78"><circle cx="39" cy="39" r="35" fill="none" stroke="#fff" stroke-width="5"/><path d="M30 22 L58 39 L30 56Z" fill="#fff"/></svg>
  <svg class="controls" width="265" height="14" viewBox="0 0 265 14"><rect width="265" height="14" fill="#111"/><g fill="#fff"><rect x="5" y="4" width="6" height="6"/><path d="M14 4l5 3-5 3z"/><rect x="30" y="4" width="6" height="6"/><rect x="70" y="6.5" width="130" height="1" fill="#777"/><circle cx="95" cy="7" r="2"/></g><text x="248" y="10" fill="#fff" font-size="7" font-family="Open Sans,sans-serif">HD</text></svg>
</div>

<!-- Why us -->
<svg class="abs why" viewBox="0 0 1200 471" preserveAspectRatio="none"><polygon points="0,0 612,34 1200,0 1200,471 612,437 0,471" fill="#2b2a28"/></svg>
<h2 class="abs display section-title why-title">Why us?</h2>

<svg class="abs feature-icon" style="left:231px;top:1598px" viewBox="0 0 70 70"><rect x="14" y="2" width="42" height="5" fill="#d9a22b"/><rect x="14" y="10" width="42" height="5" fill="#d9a22b"/><path d="M14 18h42v18h13L35 68 1 36h13z" fill="#d9a22b"/><text x="35" y="52" text-anchor="middle" font-family="Jost,sans-serif" font-weight="700" font-size="26" fill="#2b2a28">$</text></svg>
<h3 class="abs display feature-name" style="left:322px;top:1597px">Cheap</h3>
<p class="abs feature-text" style="left:322px;top:1626px">At vero eos et accusamus et iusto odio dignissimos ducimus qui blanditiis praesentium voluptatum deleniti atque corrupti quos dolores et quas molestias.</p>

<svg class="abs feature-icon" style="left:640px;top:1598px" viewBox="0 0 70 70"><path d="M35 2 L47 16 H40 V38 C40 48 34 52 28 58 L22 52 C28 46 31 43 31 38 V16 H23Z" fill="#d9a22b"/><path d="M2 30 L16 22 V28 H22 C28 28 32 32 34 36 L36 44 C34 40 30 38 24 38 H16 V44Z" fill="#d9a22b"/><path d="M68 30 L54 22 V28 H48 C42 28 39 32 38 38 V66 H47 V44 C47 40 49 38 54 38 V44Z" fill="#d9a22b"/></svg>
<h3 class="abs display feature-name" style="left:737px;top:1597px">Flexible</h3>
<p class="abs feature-text" style="left:737px;top:1626px">At vero eos et accusamus et iusto odio dignissimos ducimus qui blanditiis praesentium voluptatum deleniti atque corrupti quos dolores et quas molestias.</p>

<svg class="abs feature-icon" style="left:231px;top:1708px" viewBox="0 0 70 70"><circle cx="33" cy="35" r="31" fill="#d9a22b"/><rect x="19" y="23" width="26" height="26" fill="none" stroke="#2b2a28" stroke-width="4"/><path d="M22 34 L31 43 L52 18" fill="none" stroke="#2b2a28" stroke-width="6"/></svg>
<h3 class="abs display feature-name" style="left:322px;top:1707px">Quality</h3>
<p class="abs feature-text" style="left:322px;top:1737px">At vero eos et accusamus et iusto odio dignissimos ducimus qui blanditiis praesentium voluptatum deleniti atque corrupti quos dolores et quas molestias.</p>

<svg class="abs feature-icon" style="left:640px;top:1708px" viewBox="0 0 70 70"><path d="M4 4 V64 H66" fill="none" stroke="#d9a22b" stroke-width="3"/><rect x="14" y="44" width="8" height="16" fill="#d9a22b"/><rect x="26" y="36" width="8" height="24" fill="#d9a22b"/><rect x="38" y="40" width="8" height="20" fill="#d9a22b"/><rect x="50" y="28" width="8" height="32" fill="#d9a22b"/><path d="M12 34 L26 20 L38 28 L56 10" fill="none" stroke="#d9a22b" stroke-width="3"/><path d="M48 8 H58 V18" fill="none" stroke="#d9a22b" stroke-width="3"/></svg>
<h3 class="abs display feature-name" style="left:737px;top:1707px">Increase chance</h3>
<p class="abs feature-text" style="left:737px;top:1737px">At vero eos et accusamus et iusto odio dignissimos ducimus qui blanditiis praesentium voluptatum deleniti atque corrupti quos dolores et quas molestias.</p>

<!-- Contact -->
<h2 class="abs display section-title contact-title">Contact us</h2>
<div class="abs field" style="top:2030px">Name</div>
<div class="abs field" style="top:2084px">Email</div>
<div class="abs field" style="top:2139px">Phone</div>
<div class="abs field field-message">Message</div>
<div class="abs display send">Send</div>

<!-- Footer -->
<footer class="abs footer"></footer>
<div class="abs social"><span></span><span></span><span></span></div>
<div class="abs footer-brand">SkyNestReels</div>
<div class="abs footer-phone">&#9990; +31670418263</div>
<div class="abs copyright">Copyright © 2018 SkyNestReels</div>

</body>
</html>
```